Business card update

Opening a subsidiary of my company in the USA and need to update my logo.
Updates

Reason: Give more time to a good design.

I made a mistake on my briefing. It's only the business card. Thanks for alerting me on the mistake.

All the best

Leopoldo

Target Market(s)

We are an Executive Search company and our target audience are executives in large corporations.

Industry/Entity Type

Business

Requirements
Must have
• Keep the logo. In the US the company is called Declan Harrow Executive Search.

```html
<!DOCTYPE html>
<html lang="en">
<head>
<meta charset="utf-8">
<title>Declan Harrow Executive Search — Business Card</title>
<link rel="stylesheet" href="https://fonts.googleapis.com/css2?family=Quicksand:wght@400;500&display=swap">
<style>
  :root {
    --stage: #3f4b4f;
    --card: #ffffff;
    --teal: #3fd3ad;
    --teal-soft: #bff0e2;
    --navy: #2a3a6b;
    --ink: #1f1f1f;
    --grey: #3a3a3a;
    --red: #e0221b;
  }
  html, body {
    margin: 0;
    width: 1200px;
    height: 741px;
    overflow: hidden;
    background: var(--stage);
  }
  .canvas {
    position: relative;
    width: 1200px;
    height: 741px;
  }
  .card {
    position: absolute;
    left: 96px;
    top: 82px;
    width: 1008px;
    height: 576px;
    background: var(--card);
    font-family: "Quicksand", sans-serif;
  }
  .brand {
    position: absolute;
    left: 0;
    right: 0;
    top: 58px;
    display: flex;
    align-items: center;
    justify-content: center;
    gap: 14px;
  }
  .brand-name {
    font-size: 40px;
    font-weight: 500;
    color: var(--navy);
  }
  .brand-dot {
    width: 20px;
    height: 20px;
    border-radius: 50%;
    background: var(--teal);
  }
  .holder {
    position: absolute;
    left: 53px;
    top: 255px;
  }
  .holder-name {
    font-size: 44px;
    font-weight: 500;
    color: var(--teal);
    margin: 0;
  }
  .holder-phone {
    display: flex;
    align-items: center;
    gap: 10px;
    margin-top: 8px;
    font-size: 34px;
    font-weight: 500;
    color: var(--ink);
  }
  .contacts {
    position: absolute;
    left: 528px;
    top: 258px;
    list-style: none;
    margin: 0;
    padding: 0;
    font-size: 25px;
    line-height: 34px;
    color: var(--grey);
  }
  .contacts li {
    display: flex;
    align-items: flex-start;
    gap: 20px;
    margin-bottom: 6px;
  }
  .contacts svg { flex: none; margin-top: 4px; }
  .tagline {
    position: absolute;
    left: 8px;
    right: 8px;
    top: 528px;
    display: flex;
    align-items: center;
    gap: 14px;
    font-size: 36px;
    line-height: 42px;
    letter-spacing: 3px;
    color: var(--teal-soft);
    white-space: nowrap;
  }
  .tagline::before, .tagline::after {
    content: "";
    flex: 1;
    height: 3px;
    background: var(--teal-soft);
  }
</style>
</head>
<body>
<main class="canvas">
  <section class="card">
    <header class="brand">
      <span class="brand-name">Declan Harrow</span>
      <span class="brand-dot"></span>
    </header>

    <div class="holder">
      <h1 class="holder-name">Leopoldo S. Harrow</h1>
      <div class="holder-phone">
        <svg width="26" height="28" viewBox="0 0 24 24" aria-hidden="true">
          <path fill="var(--red)" d="M6.6 2.5l3 3.6-1.9 2.2c1 2.4 3.4 5.3 6 6.6l2.1-1.8 3.7 2.8-1.5 3.3c-.4.8-1.3 1.1-2.1.9C9.7 18.4 4.9 12.8 3.6 6.3c-.2-.9.2-1.7 1-2.1z"/>
        </svg>
        <span>305 555-0148</span>
      </div>
    </div>

    <ul class="contacts">
      <li>
        <svg width="28" height="26" viewBox="0 0 24 22" aria-hidden="true">
          <path fill="var(--teal-soft)" d="M12 1L1 11h3v10h6v-6h4v6h6V11h3z"/>
        </svg>
        <span>4820 Coral Bay Ave Suite 210<br>North Bayview FL 33190</span>
      </li>
      <li>
        <svg width="28" height="22" viewBox="0 0 24 18" aria-hidden="true">
          <rect x="1" y="1" width="22" height="16" rx="1" fill="var(--teal-soft)"/>
          <path d="M1 2l11 8 11-8" fill="none" stroke="#fff" stroke-width="1.5"/>
        </svg>
        <span>www.dhexecutivesearch.com</span>
      </li>
      <li>
        <svg width="28" height="28" viewBox="0 0 24 24" aria-hidden="true">
          <circle cx="12" cy="12" r="11" fill="var(--teal-soft)"/>
          <path d="M5 7c3 1 4 3 3 5s1 4 3 5M15 3c-1 3 1 4 3 4s3 3 1 6" fill="none" stroke="#fff" stroke-width="1.6"/>
        </svg>
        <span>lharrow@dhexecutivesearch.com</span>
      </li>
    </ul>

    <footer class="tagline">Declan Harrow Executive Search</footer>
  </section>
</main>
</body>
</html>
```